Core Values Banner For Hearthwell Partners Inc

We want to take the core values for our small growing chimney service company and post them for our entire team to see on a daily basis. We want to be remind everyone how important this is too us all. IntegrityWe try to be honest and accountable in all aspects of our business, as well as in our personal interactions. We do what we say we will do, when we say we will do it, and how we say we will do it.Kaizen“Change for the best”We strive to constantly grow and improve, both personally and professionally. We own up to our mistakes and strive to resolve and learn from them. We actively seek feedback from our clients and each other. We believe the most innovative ideas come when we intentionally look for them.FamilyWe are a family-owned business, and we consider everyone who works here and every one we serve to be part of the family. Being honest and genuine with each other and our customers is what sets us apart. We put ourselves in our customer’s shoes and make recommendations as if it were our chimney, our home and our family.

Font styles to use
Serif
Sans Serif

Colors
ec1f27

Requirements
Must have
• This banner will be approximately 2.5' in height and 6 to 6.5' in width.
• I would like all 3 core values and there definitions listed on the banner
• check out the feel of our marketing on our website www.hearthwellpartnersvt.example

```html
<!DOCTYPE html>
<html lang="en">
<head>
<meta charset="utf-8">
<title>Hearthwell Partners Inc – Our Core Values</title>
<link rel="stylesheet" href="https://fonts.googleapis.com/css2?family=Open+Sans:wght@400;600&display=swap">
<style>
  :root {
    --stage: #858585;
    --red-deep: #9a0008;
    --red-mid: #c2002b;
    --brick: #cc0033;
    --white: #ffffff;
    --ink: #1f1f1f;
    --integrity: #8e0b0d;
    --kaizen: #f39c12;
    --family: #1488d3;
    --icon-red-hi: #c4111c;
    --icon-red-lo: #8a0008;
    --icon-yellow-hi: #ffc83d;
    --icon-yellow-lo: #f29a16;
    --icon-blue-hi: #3cb6f2;
    --icon-blue-lo: #0c72c6;
  }
  * { box-sizing: border-box; margin: 0; padding: 0; }
  html, body { width: 1200px; height: 1034px; overflow: hidden; }
  body { background: var(--stage); font-family: "Open Sans", Arial, sans-serif; position: relative; color: var(--ink); }

  .banner { position: absolute; left: 32px; width: 1135px; overflow: hidden; }
  .banner--gradient { top: 31px; height: 472px; background: radial-gradient(ellipse at 50% 35%, var(--red-mid) 0%, var(--red-deep) 75%); }
  .banner--brick { top: 540px; height: 465px; background: var(--brick); }

  .brand { position: absolute; left: 0; right: 0; display: flex; justify-content: center; align-items: center; gap: 8px; color: var(--white); font-weight: 600; letter-spacing: 0.04em; text-transform: uppercase; }
  .brand__mark { width: 26px; height: 26px; border: 2px solid var(--white); }
  .banner--gradient .brand { top: 18px; font-size: 17px; }
  .banner--brick .brand { top: 22px; font-size: 17px; }

  .title { position: absolute; left: 0; right: 0; text-align: center; color: var(--white); font-weight: 400; }
  .banner--gradient .title { top: 52px; font-size: 28px; letter-spacing: 0.2em; }
  .banner--brick .title { top: 56px; font-size: 42px; letter-spacing: 0.01em; }

  .disc { position: absolute; border-radius: 50%; background: var(--white); }
  .badge { position: absolute; border-radius: 50%; background: var(--white); display: flex; align-items: center; justify-content: center; }
  .badge__inner { border-radius: 50%; }
  .badge__inner--red { background: radial-gradient(circle at 40% 35%, var(--icon-red-hi), var(--icon-red-lo)); }
  .badge__inner--yellow { background: radial-gradient(circle at 40% 35%, var(--icon-yellow-hi), var(--icon-yellow-lo)); display: flex; align-items: center; justify-content: center; }
  .badge__inner--blue { background: radial-gradient(circle at 40% 35%, var(--icon-blue-hi), var(--icon-blue-lo)); }

  .value { position: absolute; text-align: center; }
  .value__name { font-weight: 400; text-transform: uppercase; line-height: 1.4; }
  .value__name--integrity { color: var(--integrity); }
  .value__name--kaizen { color: var(--kaizen); }
  .value__name--family { color: var(--family); }
  .banner--gradient .value__name { font-size: 19px; }
  .banner--gradient .value__text { font-size: 14px; line-height: 19.2px; }
  .banner--brick .value__name { font-size: 16px; }
  .banner--brick .value__text { font-size: 12.2px; line-height: 16.6px; }
</style>
</head>
<body>

<section class="banner banner--gradient">
  <div class="brand"><span class="brand__mark"></span>Hearthwell Partners Inc</div>
  <h1 class="title">OUR CORE VALUES</h1>

  <div class="disc" style="left:32px;top:85px;width:306px;height:306px"></div>
  <div class="badge" style="left:130px;top:22px;width:118px;height:118px">
    <div class="badge__inner badge__inner--red" style="width:102px;height:102px" role="img" aria-label="Handshake icon"></div>
  </div>
  <div class="value" style="left:55px;top:166px;width:260px">
    <h2 class="value__name value__name--integrity">Integrity</h2>
    <p class="value__text">We try to be honest and accountable<br>in all aspects of our business, as well<br>as in our personal interactions.<br>We do what we say we will do, when<br>we say we will do it, and how we say<br>we will do it.</p>
  </div>

  <div class="disc" style="left:428px;top:154px;width:306px;height:306px"></div>
  <div class="badge" style="left:522px;top:88px;width:118px;height:118px">
    <div class="badge__inner badge__inner--yellow" style="width:102px;height:102px">
      <svg width="60" height="60" viewBox="0 0 60 60" aria-hidden="true">
        <circle cx="30" cy="30" r="24" fill="none" stroke="#fff" stroke-width="5" opacity="0.9"/>
        <path d="M19 30 L27 38 L44 19" fill="none" stroke="#fff" stroke-width="6" stroke-linecap="round" stroke-linejoin="round"/>
      </svg>
    </div>
  </div>
  <div class="value" style="left:441px;top:213px;width:280px">
    <h2 class="value__name value__name--kaizen">Kaizen<br>“Change for the best”</h2>
    <p class="value__text">We strive to constantly grow and<br>improve, both personally and<br>professionally. We own up to our mistakes<br>and strive to resolve and learn from them.<br>We actively seek feedback from our<br>clients and each other. We believe the<br>most innovative ideas come when we<br>intentionally look for them.</p>
  </div>

  <div class="disc" style="left:797px;top:77px;width:306px;height:306px"></div>
  <div class="badge" style="left:889px;top:22px;width:118px;height:118px">
    <div class="badge__inner badge__inner--blue" style="width:102px;height:102px" role="img" aria-label="Family icon"></div>
  </div>
  <div class="value" style="left:810px;top:146px;width:280px">
    <h2 class="value__name value__name--family">Family</h2>
    <p class="value__text">We are a family-owned business,<br>and we consider everyone who<br>works here and every one we serve to<br>be part of the family. Being honest and<br>genuine with each other and our<br>customers is what sets us apart. We<br>put ourselves in our customer’s shoes<br>and make recommendations as if it<br>were our chimney, our home and<br>our family.</p>
  </div>
</section>

<section class="banner banner--brick" role="img" aria-label="Red brick wall background">
  <div class="brand"><span class="brand__mark"></span>Hearthwell Partners Inc</div>
  <h1 class="title">OUR CORE VALUES</h1>

  <div class="disc" style="left:50px;top:71px;width:270px;height:270px"></div>
  <div class="badge" style="left:127px;top:45px;width:110px;height:110px">
    <div class="badge__inner badge__inner--red" style="width:94px;height:94px" role="img" aria-label="Handshake icon"></div>
  </div>
  <div class="value" style="left:75px;top:178px;width:220px">
    <h2 class="value__name value__name--integrity">Integrity</h2>
    <p class="value__text">We try to be honest and accountable<br>in all aspects of our business, as well<br>as in our personal interactions.<br>We do what we say we will do, when<br>we say we will do it, and how we say<br>we will do it.</p>
  </div>

  <div class="disc" style="left:423px;top:178px;width:276px;height:276px"></div>
  <div class="badge" style="left:504px;top:116px;width:110px;height:110px">
    <div class="badge__inner badge__inner--yellow" style="width:94px;height:94px">
      <svg width="56" height="56" viewBox="0 0 60 60" aria-hidden="true">
        <circle cx="30" cy="30" r="24" fill="none" stroke="#fff" stroke-width="5" opacity="0.9"/>
        <path d="M19 30 L27 38 L44 19" fill="none" stroke="#fff" stroke-width="6" stroke-linecap="round" stroke-linejoin="round"/>
      </svg>
    </div>
  </div>
  <div class="value" style="left:436px;top:227px;width:250px">
    <h2 class="value__name value__name--kaizen">Kaizen<br>“Change for the best”</h2>
    <p class="value__text">We strive to constantly grow and<br>improve, both personally and<br>professionally. We own up to our mistakes<br>and strive to resolve and learn from them.<br>We actively seek feedback from our<br>clients and each other. We believe the<br>most innovative ideas come when we<br>intentionally look for them.</p>
  </div>

  <div class="disc" style="left:812px;top:100px;width:276px;height:276px"></div>
  <div class="badge" style="left:897px;top:53px;width:110px;height:110px">
    <div class="badge__inner badge__inner--blue" style="width:94px;height:94px" role="img" aria-label="Family icon"></div>
  </div>
  <div class="value" style="left:825px;top:158px;width:250px">
    <h2 class="value__name value__name--family">Family</h2>
    <p class="value__text">We are a family-owned business,<br>and we consider everyone who<br>works here and every one we serve to<br>be part of the family. Being honest and<br>genuine with each other and our<br>customers is what sets us apart. We<br>put ourselves in our customer’s shoes<br>and make recommendations as if it<br>were our chimney, our home and<br>our family.</p>
  </div>
</section>

</body>
</html>
```